Restaurant Poster Design Project for A-Frame

I am after a poster, which will go on an outdoor A-Frame (A1 size - this size is to be confirmed) outlining our drink/happy hour/specials for our Mexican Restaurant and Bar.

Specific details are:

$4 Beer, Wine and Spirits
$5 Margaritas
everynight 5:30pm-7:30pm

I will supply logo, which needs to be incorporated (really small) into the poster, along with our address: 42 Lowden Road, Windsor - (Im not too sure if we should include our phone number or not ?? Please advise what you feel will look good etc

Happy for you to add a phrase or wording etc, as long as the specific details are included, above.

We also have an enclosed beer garden in the rear of the restaurant - Do you believe I should mention this?

I am really open to eye catching designs and ALL suggestions welcome please!
Updates

Please find attached of samples that I am sort of after: (please let me know if they cant be opened).

http://www.flyerquill.example/blog/wp-content/uploads/2012/06/happyHourPoster-e1340372894746.gif

http://marekvu.files.samplepress.example/2012/10/profolio_0012.jpg?w=1169

http://3.img.noteleaf.example/-NfNjpdG5w/T5pohPd0AhI/AAAAAAAADRs/CA7DPeI_PyU/s640/vintage_poster.jpg

http://www.orchidvane.example/files/imagecache/Event/news/teaser/Lounge_Happy_Hour_Poster_-_Mar_2011_bilingual.jpg

http://www.tkrumps.example/dallas/images/happyhour_poster.jpg

http://cdn2-b.newsgrove.example/sites/default/files/styles/large_lightbox/hash/9a/d1/9ad11350ba178511886fddcff7aaac8d.jpg?itok=wDl2vlfJ

http://www.platterpicks.example/imageservice/images/13/1313171414293_244/img_large_watermarked.jpg

Target Market(s)

18 YEARS OLD AND OVER

Industry/Entity Type

Restaurant

Requirements
Must have
• Address
Phone Number
Logo
Clear easy to read font, to be seen via cars + ppl walking down street
If images are included, to be clear and visable
Nice to have
• Images are possible
To mention a beer garden
Should not have
• Traditional Mexican Colourful 80's Theme

```html
<!DOCTYPE html>
<html lang="en">
<head>
<meta charset="utf-8">
<title>Happy Hour Specials – Mexican Restaurant &amp; Bar</title>
<link rel="stylesheet" href="https://fonts.googleapis.com/css2?family=Cinzel:wght@400;500&family=Teko:wght@500;600&display=swap">
<style>
  :root {
    --yellow: #f4e414;
    --purple: #8e176b;
    --magenta: #e0148c;
    --cyan: #19d3df;
    --green: #3fe61c;
    --ink: #111111;
    --white: #ffffff;
    --head-font: "Teko", "Arial Narrow", sans-serif;
    --serif-font: "Cinzel", "Times New Roman", serif;
  }
  html, body {
    margin: 0;
    padding: 0;
    overflow: hidden;
    background: var(--yellow);
  }
  .poster {
    position: relative;
    width: 847px;
    height: 1200px;
    overflow: hidden;
  }
  .poster-art {
    position: absolute;
    inset: 0;
    width: 847px;
    height: 1200px;
    display: block;
  }
  .headline {
    font-family: var(--head-font);
    font-weight: 600;
  }
  .headline--venue, .headline--address {
    fill: var(--green);
    stroke: #1d3b0e;
    stroke-width: 1.4px;
    paint-order: stroke;
  }
  .headline--specials { fill: var(--cyan); }
  .price, .drink {
    font-family: var(--serif-font);
    fill: var(--white);
  }
  .hours {
    font-family: var(--head-font);
    font-weight: 600;
    fill: var(--ink);
  }
  .brand-name {
    font-family: var(--head-font);
    font-weight: 600;
    fill: var(--purple);
  }
  .garden-note {
    font-family: var(--head-font);
    font-weight: 600;
    fill: var(--ink);
  }
</style>
</head>
<body>
<main class="poster">
  <svg class="poster-art" viewBox="0 0 723 1024" preserveAspectRatio="none" xmlns="http://www.w3.org/2000/svg">
    <defs>
      <linearGradient id="backdropTone" x1="0" y1="0" x2="1" y2="1">
        <stop offset="0" stop-color="#efd81a"/>
        <stop offset="0.5" stop-color="#f4e414"/>
        <stop offset="1" stop-color="#d9bc2a"/>
      </linearGradient>
    </defs>

    <rect class="backdrop" x="0" y="0" width="723" height="1024" fill="url(#backdropTone)" role="img" aria-label="Yellow backdrop with purple brushed streak texture"/>

    <!-- colour blocks -->
    <polygon class="block block--purple" fill="var(--purple)" points="0,255 90,258 90,300 515,300 722,760 722,850 472,905 405,720 0,600"/>
    <polygon class="block block--magenta-band" fill="var(--magenta)" points="0,600 140,565 420,730 470,820 640,1000 40,988 0,988"/>
    <polygon class="block block--purple-wine" fill="var(--purple)" points="395,395 515,300 715,762 465,900"/>
    <polygon class="block block--cyan" fill="var(--cyan)" points="143,565 350,437 430,712 225,806"/>

    <!-- header -->
    <text class="headline headline--venue" x="32" y="78" font-size="56" textLength="658" lengthAdjust="spacingAndGlyphs">MEXICAN RESTAURANT &amp; BAR</text>
    <text class="headline headline--address" x="32" y="138" font-size="44" textLength="462" lengthAdjust="spacingAndGlyphs">42 LOWDEN ROAD, WINDSOR</text>
    <text class="headline headline--specials" x="32" y="234" font-size="76" textLength="665" lengthAdjust="spacingAndGlyphs">HAPPY HOUR SPECIALS</text>

    <!-- brand -->
    <g class="brand">
      <circle cx="556" cy="362" r="8" fill="var(--purple)"/>
      <text class="brand-name" x="712" y="374" font-size="34" text-anchor="end" textLength="136" lengthAdjust="spacingAndGlyphs">CASA LOMITA</text>
    </g>

    <!-- $4 offer -->
    <text class="price price--four" x="6" y="362" font-size="96">$4</text>
    <g class="arrow" stroke="var(--cyan)" stroke-width="6" fill="none" stroke-linecap="round">
      <line x1="62" y1="370" x2="106" y2="436"/>
      <polyline points="70,432 106,436 110,402"/>
    </g>
    <text class="drink drink--beer" font-size="108" transform="translate(62 590) rotate(-27)" textLength="330" lengthAdjust="spacingAndGlyphs">BEER</text>

    <g class="drink drink--wine" font-size="90">
      <text class="drink" transform="translate(420 480) rotate(-22)">W</text>
      <text class="drink" transform="translate(476 570) rotate(-22)">I</text>
      <text class="drink" transform="translate(478 665) rotate(-22)">N</text>
      <text class="drink" transform="translate(505 760) rotate(-22)">E</text>
    </g>

    <!-- hours -->
    <text class="hours" x="282" y="620" font-size="44" text-anchor="middle">EVERYNIGHT</text>
    <text class="hours" x="290" y="685" font-size="44" text-anchor="middle">5:30 -7:30PM</text>

    <!-- $5 offer -->
    <text class="price price--five" x="8" y="760" font-size="96">$5</text>
    <g class="arrow" stroke="var(--cyan)" stroke-width="6" fill="none" stroke-linecap="round">
      <line x1="66" y1="780" x2="110" y2="846"/>
      <polyline points="74,842 110,846 114,812"/>
    </g>
    <text class="drink drink--margaritas" font-size="50" transform="translate(72 948) rotate(-22)" textLength="390" lengthAdjust="spacingAndGlyphs">MARGARITAS</text>
    <text class="drink drink--spirits" font-size="56" transform="translate(472 898) rotate(-22)" textLength="245" lengthAdjust="spacingAndGlyphs">SPIRITS</text>

    <!-- footer -->
    <text class="garden-note" x="382" y="988" font-size="38" textLength="324" lengthAdjust="spacingAndGlyphs">VISIT OUR BEER GARDEN!</text>
  </svg>
</main>
</body>
</html>
```